PowerPoint template for Law Firm

We Need a PowerPoint Template for a Law Firm in Switzerland. We are primarly consult in business law. We Need a template for PowerPoint to Show Information to our Clients (inheritence law, corporate law, legal structures etc.) The design should be contemporary, simple and clear. It should be in harmony with our website: www.trovanek.com Style: professional, structured and clearly arranged. Colors: Blue (R: 1, G: 61: B: 105), white. Font: Calibri Ratio: 16: 9 Esamples attached

```html
<!DOCTYPE html>
<html lang="en">
<head>
<meta charset="utf-8">
<title>Trovanek—Lawyers · Presentation Template</title>
<link rel="stylesheet" href="https://fonts.googleapis.com/css2?family=Archivo+Black&family=Carlito:wght@400;700&display=swap">
<style>
:root{
  --navy:#013d69;
  --steel:#2f6592;
  --sky:#8ec5ef;
  --sky-soft:#b3daf7;
  --lilac:#a9bce6;
  --azure:#2d8ff0;
  --royal:#3566b8;
  --cyan:#7ccdf0;
  --ink:#1c1c1c;
  --grey:#7a7a7a;
  --rule:#c9dff1;
  --sheet:#f3f3f3;
  --photo-a:#c9c4bd;
  --photo-b:#6e6a66;
}
*{box-sizing:border-box;margin:0;padding:0}
html,body{width:1200px;height:2201px;overflow:hidden}
body{background:var(--sheet);font-family:"Carlito",Calibri,Arial,sans-serif;color:var(--ink);position:relative}
.abs{position:absolute}

.hero{position:absolute;left:65px;top:47px;width:621px;height:349px;background:#fff;box-shadow:0 1px 4px rgba(0,0,0,.18)}
.hero .hero-brand{left:396px;top:44px;font-size:21px;color:var(--navy)}
.hero .hero-line{left:31px;top:160px;width:550px;height:100px;background:linear-gradient(90deg,rgba(1,61,105,0),rgba(1,61,105,.12) 30%,rgba(1,61,105,.16) 60%,rgba(1,61,105,0));border-radius:50px}
.hero .hero-tagline{left:33px;top:276px;font-size:12px;line-height:14px;color:#333}

.features{position:absolute;left:760px;top:0;width:440px;height:430px;font-family:"Archivo Black",Arial,sans-serif;font-size:21px;color:#1a1a1a}
.features .item{position:absolute;left:26px;white-space:nowrap}
.features .item::before{content:"";position:absolute;left:-25px;top:3px;width:19px;height:19px;border:3px solid #1a1a1a;border-radius:2px}
.features .cont{position:absolute;left:18px;white-space:nowrap}
.features .sub{position:absolute;left:77px;white-space:nowrap}
.features .sub::before{content:"";position:absolute;left:-17px;top:8px;width:8px;height:8px;background:#1a1a1a}

.slide{position:absolute;width:358px;height:201px;background:#fff;overflow:hidden;box-shadow:0 1px 3px rgba(0,0,0,.2)}
.slide.dark{background:var(--navy)}
.brand{position:absolute;font-size:6.6px;font-weight:700;color:var(--navy);white-space:nowrap}
.brand.tr{right:18px;top:9px}
.brand.tl{left:30px;top:9px}
.title{position:absolute;font-size:12.5px;line-height:13px;color:var(--ink)}
.title.white{color:#fff}
.sub-title{position:absolute;font-size:7px;color:var(--grey)}
.copy{position:absolute;font-size:3.7px;line-height:5.6px;color:var(--navy);text-align:justify}
.copy.white{color:#fff}
.copy.dim{color:#555}
.pg{position:absolute;bottom:4px;right:7px;font-size:5.5px;color:#7aa9d6}
.pg.left{right:auto;left:12px}
.pg.white{color:#fff}
.panel{position:absolute;top:0;height:201px;background:var(--navy)}
.panel.steel{background:var(--steel)}
.photo{position:absolute;background:linear-gradient(135deg,var(--photo-a),var(--photo-b))}
.photo.office{background:linear-gradient(160deg,#dfe3e6,#8e9aa3 55%,#4c4a48)}
.photo.paper{background:linear-gradient(120deg,#2a2a2a,#9b9b9b 45%,#efefef 70%,#d6d6d6)}
.photo.gallery{background:linear-gradient(150deg,#f0efed,#d9d7d4 60%,#b9b7b3)}
.photo.hands{background:linear-gradient(150deg,#e9ecf0,#c8b4a4 50%,#8aa0bd)}
.ornament{position:absolute;background:linear-gradient(90deg,rgba(255,255,255,0),rgba(255,255,255,.35),rgba(255,255,255,0));height:10px;border-radius:5px}
.ornament.ondark{background:linear-gradient(90deg,rgba(1,61,105,0),rgba(1,61,105,.22),rgba(1,61,105,0))}
.vrule{position:absolute;width:1px;background:var(--rule)}
.hrule{position:absolute;height:1px;background:var(--rule)}
.hrule.white{background:rgba(255,255,255,.35)}

.toc-num{position:absolute;left:181px;width:14px;height:14px;border:1px solid var(--navy);font-size:5.5px;color:var(--navy);display:flex;align-items:center;justify-content:center}
.toc-label{position:absolute;left:205px;font-size:6.2px;color:var(--navy);line-height:7px}
.toc-label small{display:block;font-size:3.5px;color:#666;line-height:5px}

.bio-h{position:absolute;font-size:4px;font-weight:700;line-height:5px}
.bio{position:absolute;font-size:3.6px;line-height:4.8px}

.spec-list{position:absolute;left:179px;top:51px;list-style:none;font-size:6.4px;line-height:14.3px;color:#1f5f9a}
.spec-list li{position:relative;padding-left:9px}
.spec-list li::before{content:"";position:absolute;left:0;top:6px;width:2.5px;height:2.5px;border-radius:50%;background:#1f5f9a}

.node{position:absolute;display:flex;align-items:center;justify-content:center;font-size:3.6px;color:#fff}
.node.root{background:var(--navy)}
.node.mid{background:var(--lilac)}
.node.leaf{background:var(--sky-soft)}
.node.azure{background:var(--azure)}
.node.cyan{background:var(--cyan)}
.node.royal{background:#3d8ff0}
.node.indigo{background:#5a7fe0}
.card{position:absolute;width:69px;height:19px;display:flex}
.card .face{width:18px;height:19px;background:linear-gradient(135deg,#d9d4cf,#7a746f);border:1.5px solid #fff}
.card .tag{flex:1;display:flex;flex-direction:column;justify-content:center;padding-left:3px;font-size:4px;font-weight:700;color:#fff;line-height:4.6px}
.card .tag small{font-weight:400;font-size:3px}
.card.navy .tag{background:#1a3f73}
.card.cyan .tag{background:var(--cyan)}
.card.royal .tag{background:var(--royal)}
.card.sky .tag{background:#4c8fe0}

.tl-year{position:absolute;left:143px;font-size:5.4px;color:var(--grey)}
.tl-dot{position:absolute;left:177px;width:4.5px;height:4.5px;border-radius:50%;background:#7fb4e3}
.tl-head{position:absolute;left:190px;font-size:6px;color:var(--navy)}
.tl-note{position:absolute;left:190px;width:110px;font-size:3.4px;line-height:5px;color:#555}

.tile{position:absolute;background:var(--navy)}
.tile.steel{background:var(--steel)}
.tile.grey{background:linear-gradient(135deg,#f1f1f1,#cfcfcf)}
.kw{position:absolute;width:55px;height:54px;display:flex;align-items:center;justify-content:center;font-size:5.5px}
.kw.deep{background:var(--navy);color:#fff}
.kw.pale{background:var(--sky);color:var(--navy)}
.proj-h{position:absolute;font-size:6px;color:var(--navy)}
</style>
</head>
<body>

<section class="hero">
  <div class="abs hero-brand">Trovanek—Lawyers</div>
  <div class="abs hero-line" role="img" aria-label="Single-line drawing of an alpine mountain ridge"></div>
  <p class="abs hero-tagline">A clear line fosters solutions –<br>regardless of how straightforward it is.</p>
</section>

<div class="features">
  <div class="item" style="top:30px">Ratio 16:9</div>
  <div class="item" style="top:60px">Full HD</div>
  <div class="item" style="top:90px">Custom color pallet</div>
  <div class="item" style="top:121px">Custom Font -&nbsp; Easy Change</div>
  <div class="item" style="top:151px">Easy to edit, just drag and drop</div>
  <div class="cont" style="top:177px">images</div>
  <div class="item" style="top:207px">Can be included up to 50</div>
  <div class="cont" style="top:235px">slides;</div>
  <div class="sub" style="top:263px">Text + images (1,2,3,4) ,</div>
  <div class="sub cont" style="top:290px;left:77px">Text Slides</div>
  <div class="sub" style="top:317px">Portfolio Slides , blog slides</div>
  <div class="sub" style="top:343px">Text Slides, infographics</div>
  <div class="sub" style="top:370px">Data Slides</div>
  <div class="item" style="top:398px">In the sample you find 25 slides</div>
</div>

<section class="slide" style="left:16px;top:461px">
  <div class="photo office" style="left:0;top:0;width:358px;height:137px" role="img" aria-label="Photo of two colleagues in a business meeting"></div>
  <div class="abs" style="left:14px;top:150px;font-size:12px;color:var(--navy)">Trovanek—Lawyers</div>
  <p class="copy" style="left:150px;top:143px;width:180px">We advise demanding clients in Switzerland and abroad with clear, targeted solutions. Flexibility and fast response times set us apart. A high degree of professionalism and discretion is a matter of course for us. We use modern tools and are well versed in current media. We are a reliable partner in all areas of commercial law.</p>
  <div class="pg">2</div>
</section>

<section class="slide" style="left:416px;top:461px">
  <div class="panel" style="left:0;width:127px"></div>
  <div class="title white" style="left:0;width:127px;top:94px;text-align:center">Contents</div>
  <div class="brand tr">Trovanek—Lawyers</div>
  <div class="toc-num" style="top:31px">1</div><div class="toc-label" style="top:32px">Introduction<small>Before starting</small></div>
  <div class="toc-num" style="top:62px">2</div><div class="toc-label" style="top:63px">About us<small>What we did, what we do</small></div>
  <div class="toc-num" style="top:93px">3</div><div class="toc-label" style="top:94px">Our portfolio<small>Our amazing products</small></div>
  <div class="toc-num" style="top:124px">4</div><div class="toc-label" style="top:125px">New proposal<small>Our awesome ideas</small></div>
  <div class="toc-num" style="top:155px">5</div><div class="toc-label" style="top:156px">Analysis<small>Marketing data and our estimation</small></div>
  <div class="pg">3</div>
</section>

<section class="slide" style="left:816px;top:461px">
  <div class="brand tr">Trovanek—Lawyers</div>
  <div class="title" style="right:208px;top:94px">Our vision</div>
  <div class="vrule" style="left:158px;top:47px;height:107px"></div>
  <div class="ornament ondark" style="left:170px;top:72px;width:175px;height:14px" role="img" aria-label="Line drawing of a mountain ridge"></div>
  <p class="copy" style="left:162px;top:111px;width:180px">We advise demanding clients in Switzerland and abroad with targeted solutions. Flexibility and fast response times set us apart. Discretion is a matter of course for us. We use modern tools and are a reliable partner in all areas of commercial law, building trust and security for our clients.</p>
  <div class="pg">6</div>
</section>

<section class="slide dark" style="left:16px;top:678px">
  <div class="photo" style="left:27px;top:0;width:113px;height:201px;background:linear-gradient(160deg,#9aa6ad,#3a4148 60%,#1d2a36)" role="img" aria-label="Portrait of a lawyer in a dark suit"></div>
  <div class="ornament" style="left:230px;top:14px;width:108px" role="img" aria-label="Mountain line decoration"></div>
  <div class="title white" style="left:179px;top:38px">Lukas Brenner,</div>
  <div class="abs" style="left:179px;top:56px;font-size:6px;color:#cfe0ee">Lawyer and Notary</div>
  <p class="copy white" style="left:179px;top:70px;width:168px">Lukas Brenner studied law before graduating in 2009. He then worked as a trainee at a cantonal court and as an auditor. He has held positions within a private bank and a law firm in Geneva. After six years as a partner, he founded his own firm in 2019.</p>
  <div class="bio-h" style="left:179px;top:109px;color:#fff">Experience</div>
  <div class="bio" style="left:179px;top:114px;color:#fff">Partner at a commercial law firm (since 2012)<br>Legal counsel at a private bank (2011)<br>Legal internship at a cantonal court (2011)</div>
  <div class="bio-h" style="left:179px;top:130px;color:#fff">Education</div>
  <div class="bio" style="left:179px;top:135px;color:#fff">Bar admission as attorney and notary (2012)<br>M.A. in Law, Feldmark University (2009)<br>B.A. in Law, Feldmark University (2007)</div>
  <div class="bio-h" style="left:179px;top:156px;color:#fff">Languages</div>
  <div class="bio" style="left:179px;top:161px;color:#fff">German / English / French</div>
  <div class="bio-h" style="left:267px;top:156px;color:#fff">Membership</div>
  <div class="bio" style="left:267px;top:161px;color:#fff">Alpine Bar Guild<br>Eastern Bar Circle<br>Young Leaders Circle</div>
  <div class="pg white">4</div>
</section>

<section class="slide" style="left:416px;top:678px">
  <div class="brand tl">Trovanek—Lawyers</div>
  <div class="title" style="left:28px;top:30px">Lukas Brenner,</div>
  <div class="sub-title" style="left:28px;top:48px">Lawyer and Notary</div>
  <p class="copy dim" style="left:28px;top:62px;width:172px">Lukas Brenner studied law before graduating in 2009. He then worked as a trainee at a cantonal court and as an auditor. He has held positions within a private bank and a law firm in Geneva. After six years as a partner, he founded his own firm in 2019.</p>
  <div class="bio-h" style="left:28px;top:101px;color:#333">Experience</div>
  <div class="bio" style="left:28px;top:106px;color:#444">Partner at a commercial law firm (since 2012)<br>Legal counsel at a private bank (2011)<br>Legal internship at a cantonal court (2011)</div>
  <div class="bio-h" style="left:28px;top:122px;color:#333">Education</div>
  <div class="bio" style="left:28px;top:127px;color:#444">Bar admission as attorney and notary (2012)<br>M.A. in Law, Feldmark University (2009)<br>B.A. in Law, Feldmark University (2007)</div>
  <div class="bio-h" style="left:28px;top:148px;color:#333">Languages</div>
  <div class="bio" style="left:28px;top:153px;color:#444">German / English / French</div>
  <div class="bio-h" style="left:115px;top:148px;color:#333">Membership</div>
  <div class="bio" style="left:115px;top:153px;color:#444">Alpine Bar Guild<br>Eastern Bar Circle<br>Young Leaders Circle</div>
  <div class="photo" style="left:218px;top:0;width:112px;height:201px;background:linear-gradient(160deg,#e7e9ea,#8d959b 55%,#2a323a)" role="img" aria-label="Portrait of a lawyer in a dark suit"></div>
  <div class="pg left">5</div>
</section>

<section class="slide" style="left:816px;top:678px">
  <div class="panel steel" style="left:27px;width:112px" role="img" aria-label="Line drawings of hands reaching across the panel"></div>
  <div class="brand tr">Trovanek—Lawyers</div>
  <div class="title" style="left:176px;top:69px">What makes us<br>different?</div>
  <div class="hrule" style="left:176px;top:98px;width:182px"></div>
  <p class="copy" style="left:176px;top:107px;width:168px">We advise demanding clients in Switzerland and abroad with targeted solutions. Flexibility and fast response times set us apart. Discretion is a matter of course for us. We use modern tools and are a reliable partner in all areas of commercial law, building trust and security for our clients.</p>
  <div class="pg">7</div>
</section>

<section class="slide" style="left:16px;top:896px">
  <div class="title" style="left:29px;top:61px">Optimum<br>guidance in<br>matters of<br>commercial law<br>– and beyond</div>
  <div class="panel" style="left:128px;width:127px"></div>
  <p class="copy white" style="left:147px;top:60px;width:90px"><b>Trovanek Lawyers specialises</b> in national and international commercial law. We support entrepreneurs with guidance in labour law matters, tough contract talks and complex deals. As part of your board we bring our expertise to your company and support you in your growth. Where your business goes, we go too.</p>
  <div class="photo paper" style="left:255px;top:0;width:103px;height:201px" role="img" aria-label="Fountain pen resting on a document"></div>
  <div class="pg left">8</div>
</section>

<section class="slide" style="left:416px;top:896px">
  <div class="panel" style="left:0;width:127px"></div>
  <div class="title white" style="left:0;width:127px;top:86px;text-align:center">Specialist area –<br>commercial law:</div>
  <div class="brand tr">Trovanek—Lawyers</div>
  <ul class="spec-list">
    <li>Corporate law</li>
    <li>Mergers and acquisitions</li>
    <li>Commercial and contrac law</li>
    <li>Labour law</li>
    <li>Financial and Market Capital Law</li>
    <li>Competition and Intellectual property law</li>
    <li>Digital economy, IT law, Data protection<br>Law</li>
  </ul>
  <div class="pg">9</div>
</section>

<section class="slide" style="left:816px;top:896px">
  <div class="brand tl">Trovanek—Lawyers</div>
  <div class="title" style="left:29px;top:55px">Unique<br>and<br>sophisticated</div>
  <div class="hrule" style="left:29px;top:100px;width:189px"></div>
  <p class="copy" style="left:29px;top:107px;width:180px">We bring clarity to complex questions and keep every step easy to follow. Our team works closely with each client to find the best route forward. Careful work, open words and a steady hand guide all that we do for you.</p>
  <div class="photo gallery" style="left:218px;top:0;width:112px;height:201px" role="img" aria-label="Framed line drawings hanging on a wall"></div>
  <div class="pg left">10</div>
</section>

<section class="slide" style="left:16px;top:1113px">
  <div class="brand tr">Trovanek—Lawyers</div>
  <div class="title" style="left:29px;top:75px">Tree<br>diagram</div>
  <p class="copy dim" style="left:29px;top:103px;width:96px">Show how ideas, teams or cases branch out from one root into clear parts. Each node can hold a short label.</p>
  <svg class="abs" style="left:0;top:0" width="358" height="201" viewBox="0 0 358 201" aria-hidden="true">
    <g stroke="#c7cfd8" stroke-width="0.8" fill="none">
      <path d="M168 43 V125 M168 71.5 H179 M168 125 H179"/>
      <path d="M237 71.5 H255 M255 71 V92 M255 71 H272 M255 92 H272"/>
      <path d="M237 125 H255 M255 125 V167 M255 125 H272 M255 145 H272 M255 167 H272"/>
    </g>
  </svg>
  <div class="node root" style="left:139px;top:28px;width:59px;height:14px">Root node</div>
  <div class="node mid" style="left:179px;top:65px;width:58px;height:13px">Node 1</div>
  <div class="node mid" style="left:179px;top:119px;width:58px;height:13px">Node 2</div>
  <div class="node leaf" style="left:272px;top:65px;width:58px;height:13px">Leaf node 1.1</div>
  <div class="node leaf" style="left:272px;top:86px;width:58px;height:13px">Leaf node 1.2</div>
  <div class="node leaf" style="left:272px;top:119px;width:58px;height:13px">Leaf node 2.1</div>
  <div class="node leaf" style="left:272px;top:139px;width:58px;height:13px">Leaf node 2.2</div>
  <div class="node leaf" style="left:272px;top:161px;width:58px;height:13px">Leaf node 2.3</div>
  <div class="pg">16</div>
</section>

<section class="slide" style="left:416px;top:1113px">
  <div class="title" style="left:26px;top:15px">Organization Structure</div>
  <div class="abs" style="left:30px;top:32px;font-size:3.4px;color:#555">Put your great subtitle here</div>
  <div class="brand tr">Trovanek—Lawyers</div>
  <svg class="abs" style="left:0;top:0" width="358" height="201" viewBox="0 0 358 201" aria-hidden="true">
    <g stroke="#1a3f73" stroke-width="0.8" fill="none">
      <path d="M81 110 H89 V88 H97 M89 110 V133 H97"/>
      <path d="M166 88 H175 V63 H184 M175 88 V90 H184"/>
      <path d="M166 133 H175 V160 H184 M175 133 H184"/>
      <path d="M253 90 H261 M253 133 H261"/>
    </g>
  </svg>
  <div class="card navy" style="left:12px;top:101px"><div class="face" role="img" aria-label="Portrait photo"></div><div class="tag">Jhon Sam<small>CEO</small></div></div>
  <div class="card navy" style="left:97px;top:79px"><div class="face" role="img" aria-label="Portrait photo"></div><div class="tag">John Smith<small>Manager</small></div></div>
  <div class="card navy" style="left:97px;top:124px"><div class="face" role="img" aria-label="Portrait photo"></div><div class="tag">Alex Day<small>Manager</small></div></div>
  <div class="card cyan" style="left:184px;top:54px"><div class="face" role="img" aria-label="Portrait photo"></div><div class="tag">Patrick<small>General Manager</small></div></div>
  <div class="card cyan" style="left:184px;top:81px"><div class="face" role="img" aria-label="Portrait photo"></div><div class="tag">James<small>General Manager</small></div></div>
  <div class="card royal" style="left:184px;top:124px"><div class="face" role="img" aria-label="Portrait photo"></div><div class="tag">Neal<small>General Manager</small></div></div>
  <div class="card royal" style="left:184px;top:151px"><div class="face" role="img" aria-label="Portrait photo"></div><div class="tag">Jessica<small>General Manager</small></div></div>
  <div class="card sky" style="left:261px;top:81px"><div class="face" role="img" aria-label="Portrait photo"></div><div class="tag">Jackie<small>Member</small></div></div>
  <div class="card sky" style="left:261px;top:124px"><div class="face" role="img" aria-label="Portrait photo"></div><div class="tag">Ericka<small>Member</small></div></div>
  <div class="pg">17</div>
</section>

<section class="slide" style="left:816px;top:1113px">
  <div class="title" style="left:26px;top:15px">Organization Structure</div>
  <div class="abs" style="left:30px;top:32px;font-size:3.4px;color:#555">Put your great subtitle here</div>
  <div class="brand tr">Trovanek—Lawyers</div>
  <svg class="abs" style="left:0;top:0" width="358" height="201" viewBox="0 0 358 201" aria-hidden="true">
    <g stroke="#7a8a99" stroke-width="0.7" fill="none">
      <path d="M173 61 V74 M173 84 V90 M74 90 H266 M74 90 V96 M147 90 V96 M220 90 V96 M266 90 V96"/>
      <path d="M74 106 V108 M62 118 V148 H62"/>
      <path d="M147 106 V108 M124 108 H174"/>
      <path d="M220 106 V170 M220 108 H209 M266 106 V108"/>
    </g>
  </svg>
  <div class="node root" style="left:150px;top:51px;width:46px;height:10px">General Manager</div>
  <div class="node root" style="left:128px;top:74px;width:42px;height:10px">Assistent</div>
  <div class="node azure" style="left:51px;top:96px;width:47px;height:10px">Sales</div>
  <div class="node cyan" style="left:124px;top:96px;width:47px;height:10px">Production</div>
  <div class="node royal" style="left:199px;top:96px;width:42px;height:10px">Finance</div>
  <div class="node indigo" style="left:243px;top:96px;width:47px;height:10px">Supply Chain</div>
  <div class="node azure" style="left:53px;top:108px;width:40px;height:12px"></div>
  <div class="node azure" style="left:62px;top:126px;width:40px;height:12px"></div>
  <div class="node azure" style="left:62px;top:143px;width:40px;height:12px"></div>
  <div class="node cyan" style="left:102px;top:108px;width:40px;height:12px"></div>
  <div class="node cyan" style="left:108px;top:126px;width:40px;height:12px"></div>
  <div class="node cyan" style="left:152px;top:108px;width:40px;height:12px"></div>
  <div class="node cyan" style="left:167px;top:126px;width:40px;height:12px"></div>
  <div class="node royal" style="left:209px;top:108px;width:40px;height:12px"></div>
  <div class="node royal" style="left:209px;top:126px;width:40px;height:12px"></div>
  <div class="node royal" style="left:209px;top:143px;width:40px;height:12px"></div>
  <div class="node royal" style="left:209px;top:163px;width:40px;height:12px"></div>
  <div class="node indigo" style="left:260px;top:108px;width:40px;height:12px"></div>
  <div class="node indigo" style="left:260px;top:126px;width:40px;height:12px"></div>
  <div class="pg">18</div>
</section>

<section class="slide" style="left:16px;top:1330px">
  <div class="brand tr">Trovanek—Lawyers</div>
  <div class="title" style="left:29px;top:72px">Our<br>history</div>
  <p class="copy dim" style="left:29px;top:105px;width:96px">A short look back at how the firm began, grew and found its place. Add the key steps that shaped our path.</p>
  <div class="vrule" style="left:179px;top:0;height:201px"></div>
  <div class="tl-year" style="top:52px">2010</div><div class="tl-dot" style="top:54px"></div><div class="tl-head" style="top:52px">Born</div><p class="tl-note" style="top:61px">Short note on the start of the firm<br>and its first clients.</p>
  <div class="tl-year" style="top:98px">2012</div><div class="tl-dot" style="top:100px"></div><div class="tl-head" style="top:98px">Growth</div><p class="tl-note" style="top:107px">Short note on a larger team and<br>new areas of practice.</p>
  <div class="tl-year" style="top:144px">2014</div><div class="tl-dot" style="top:146px"></div><div class="tl-head" style="top:144px">Innovation</div><p class="tl-note" style="top:153px">Short note on new tools and<br>ways of working.</p>
  <div class="pg">12</div>
</section>

<section class="slide" style="left:416px;top:1330px">
  <div class="brand tr">Trovanek—Lawyers</div>
  <div class="title" style="left:0;width:358px;top:30px;text-align:center">Project details</div>
  <div class="abs" style="left:0;width:358px;top:47px;text-align:center;font-size:3.5px;color:#555">Put a short line here that sums up the projects below.</div>
  <div class="tile" style="left:128px;top:70px;width:45px;height:45px" role="img" aria-label="Laptop line icon"></div>
  <div class="tile" style="left:185px;top:70px;width:45px;height:45px" role="img" aria-label="Target line icon"></div>
  <div class="tile" style="left:128px;top:126px;width:45px;height:45px" role="img" aria-label="Arrows line icon"></div>
  <div class="tile" style="left:185px;top:126px;width:45px;height:45px" role="img" aria-label="Pie chart line icon"></div>
  <div class="proj-h" style="right:247px;top:78px">Project 01</div>
  <p class="copy dim" style="right:247px;top:87px;width:90px;text-align:right">Brief outline of the first project and the result it brought to the client team.</p>
  <div class="proj-h" style="left:246px;top:78px">Project 02</div>
  <p class="copy dim" style="left:246px;top:87px;width:90px;text-align:left">Brief outline of the second project and the result it brought to the client team.</p>
  <div class="proj-h" style="right:247px;top:134px">Project 03</div>
  <p class="copy dim" style="right:247px;top:143px;width:90px;text-align:right">Brief outline of the third project and the result it brought to the client team.</p>
  <div class="proj-h" style="left:246px;top:134px">Project 04</div>
  <p class="copy dim" style="left:246px;top:143px;width:90px;text-align:left">Brief outline of the fourth project and the result it brought to the client team.</p>
  <div class="pg">17</div>
</section>

<section class="slide" style="left:816px;top:1330px">
  <div class="brand tr">Trovanek—Lawyers</div>
  <div class="title" style="right:208px;top:86px;text-align:right">A leader is<br>a dealer in hope</div>
  <div class="vrule" style="left:158px;top:51px;height:107px"></div>
  <p class="copy dim" style="left:164px;top:84px;width:165px">Good counsel looks ahead. We give our clients a clear view of their options and the confidence to act. With care and focus we turn hard questions into firm next steps, so every decision rests on solid ground and a shared sense of purpose.</p>
  <div class="pg">19</div>
</section>

<section class="slide" style="left:16px;top:1547px">
  <div class="brand tr">Trovanek—Lawyers</div>
  <div class="vrule" style="left:179px;top:0;height:201px"></div>
  <div class="tl-year" style="top:52px">2010</div><div class="tl-dot" style="top:54px"></div><div class="tl-head" style="top:52px">Born</div><p class="tl-note" style="top:61px">Short note on the start of the firm<br>and its first clients.</p>
  <div class="tl-year" style="top:98px">2012</div><div class="tl-dot" style="top:100px"></div><div class="tl-head" style="top:98px">Growth</div><p class="tl-note" style="top:107px">Short note on a larger team and<br>new areas of practice.</p>
  <div class="tl-year" style="top:144px">2014</div><div class="tl-dot" style="top:146px"></div><div class="tl-head" style="top:144px">Innovation</div><p class="tl-note" style="top:153px">Short note on new tools and<br>ways of working.</p>
  <div class="pg">13</div>
</section>

<section class="slide" style="left:416px;top:1547px">
  <div class="brand tl">Trovanek—Lawyers</div>
  <div class="title" style="left:30px;top:90px">Our product<br>principles</div>
  <div class="panel" style="left:128px;width:127px"></div>
  <div class="abs" style="left:147px;top:47px;font-size:5.5px;color:#fff">Creativity</div>
  <p class="copy white" style="left:147px;top:56px;width:90px">We look at each case with fresh eyes and find paths others miss. New ideas serve one goal: a result that works for you.</p>
  <div class="abs" style="left:147px;top:107px;font-size:5.5px;color:#fff">Originality</div>
  <p class="copy white" style="left:147px;top:116px;width:90px">No two clients are alike, so no two answers are. We shape every solution around your needs, your pace and your plans for the years ahead.</p>
  <div class="photo office" style="left:255px;top:0;width:103px;height:201px" role="img" aria-label="Photo of a smiling lawyer at a meeting table"></div>
  <div class="pg left">20</div>
</section>

<section class="slide" style="left:816px;top:1547px">
  <div class="brand tr">Trovanek—Lawyers</div>
  <div class="title" style="left:29px;top:55px">Our<br>awesome<br>projects</div>
  <div class="hrule" style="left:29px;top:101px;width:146px"></div>
  <p class="copy dim" style="left:29px;top:107px;width:140px">A selection of the work we are proud of. Each project shows how careful advice and a clear plan lead to lasting results for our clients and partners.</p>
  <div class="tile" style="left:173px;top:28px;width:81px;height:80px" role="img" aria-label="Laptop line drawing"></div>
  <div class="tile grey" style="left:254px;top:34px;width:66px;height:64px" role="img" aria-label="Sketch of a building"></div>
  <div class="tile grey" style="left:198px;top:108px;width:56px;height:54px" role="img" aria-label="Sketch of buildings"></div>
  <div class="tile" style="left:254px;top:108px;width:66px;height:67px" role="img" aria-label="Stamp line drawing"></div>
  <div class="pg">22</div>
</section>

<section class="slide" style="left:16px;top:1764px">
  <div class="brand tr">Trovanek—Lawyers</div>
  <div class="title" style="left:29px;top:92px">Still<br>growing</div>
  <div class="vrule" style="left:179px;top:0;height:201px"></div>
  <div class="tl-year" style="top:52px">2016</div><div class="tl-dot" style="top:54px"></div><div class="tl-head" style="top:52px">Award</div><p class="tl-note" style="top:61px">Short note on the prize we won<br>and why it mattered.</p>
  <div class="tl-year" style="top:98px">2018</div><div class="tl-dot" style="top:100px"></div><div class="tl-head" style="top:98px">Success</div><p class="tl-note" style="top:107px">Short note on a major case and<br>its outcome.</p>
  <div class="tl-year" style="top:144px">2020</div><div class="tl-dot" style="top:146px"></div><div class="tl-head" style="top:144px">Now</div><p class="tl-note" style="top:153px">Short note on where we stand<br>today and what comes next.</p>
  <div class="pg">14</div>
</section>

<section class="slide" style="left:416px;top:1764px">
  <div class="brand tr">Trovanek—Lawyers</div>
  <div class="tile" style="left:27px;top:27px;width:82px;height:68px" role="img" aria-label="Laptop line drawing"></div>
  <div class="tile" style="left:27px;top:101px;width:82px;height:72px" role="img" aria-label="Arrows line drawing"></div>
  <div class="tile steel" style="left:113px;top:27px;width:66px;height:146px" role="img" aria-label="Line drawings of hands"></div>
  <div class="title" style="left:220px;top:62px">Our<br>awesome<br>projects</div>
  <div class="hrule" style="left:220px;top:111px;width:138px"></div>
  <p class="copy dim" style="left:220px;top:115px;width:112px">A selection of the work we are proud of. Each project shows how careful advice and a clear plan lead to lasting results for our clients.</p>
  <div class="pg">21</div>
</section>

<section class="slide dark" style="left:816px;top:1764px">
  <div class="photo hands" style="left:27px;top:0;width:76px;height:132px" role="img" aria-label="Hand holding a pen"></div>
  <div class="photo paper" style="left:103px;top:64px;width:77px;height:137px" role="img" aria-label="Fountain pen on a document"></div>
  <div class="abs" style="left:143px;top:56px;font-size:5px;color:#fff">Project # 1</div>
  <div class="abs" style="left:30px;top:145px;font-size:5px;color:#fff">Project # 2</div>
  <div class="ornament" style="left:230px;top:15px;width:108px" role="img" aria-label="Mountain line decoration"></div>
  <div class="title white" style="left:220px;top:62px">Our<br>next<br>project</div>
  <div class="hrule white" style="left:220px;top:111px;width:138px"></div>
  <p class="copy white" style="left:220px;top:115px;width:112px">Here we show the next step we plan with our clients. A short line on the aim, the team and the time frame fits well here.</p>
  <div class="pg white">23</div>
</section>

<section class="slide" style="left:16px;top:1981px">
  <div class="brand tr">Trovanek—Lawyers</div>
  <div class="kw deep" style="left:60px;top:38px">Keyword 01</div>
  <div class="kw pale" style="left:117px;top:53px">Keyword 02</div>
  <div class="kw pale" style="left:60px;top:96px">Keyword 03</div>
  <div class="kw deep" style="left:117px;top:110px">Keyword 04</div>
  <div class="title" style="left:220px;top:73px">4 important<br>keywords</div>
  <p class="copy dim" style="left:220px;top:102px;width:96px">Four words that sum up how we work. Use this slide to stress the ideas your clients should keep in mind.</p>
  <div class="pg">24</div>
</section>

<section class="slide" style="left:416px;top:1981px">
  <div class="brand tr">Trovanek—Lawyers</div>
  <div class="title" style="left:29px;top:90px">Our<br>promises</div>
  <div class="photo hands" style="left:101px;top:0;width:117px;height:201px" role="img" aria-label="Two hands passing a pen over papers"></div>
  <div class="abs" style="left:219px;top:30px;font-size:5.5px;color:var(--navy)">We care</div>
  <p class="copy dim" style="left:219px;top:39px;width:118px">We listen first and take time to know your goals, so our advice fits you.</p>
  <div class="abs" style="left:219px;top:81px;font-size:5.5px;color:var(--navy)">We share</div>
  <p class="copy dim" style="left:219px;top:90px;width:118px">We keep you informed at each stage and explain our steps in plain words.</p>
  <div class="abs" style="left:219px;top:135px;font-size:5.5px;color:var(--navy)">We open</div>
  <p class="copy dim" style="left:219px;top:144px;width:118px">We open doors to new options and a trusted network of partners.</p>
  <div class="pg">11</div>
</section>

<section class="slide" style="left:816px;top:1981px">
  <div class="panel" style="left:0;width:127px"></div>
  <div class="tile" style="left:62px;top:57px;width:98px;height:86px" role="img" aria-label="Laptop line drawing"></div>
  <div class="ornament" style="left:14px;top:178px;width:90px" role="img" aria-label="Mountain line decoration"></div>
  <div class="brand tr">Trovanek—Lawyers</div>
  <div class="title" style="left:180px;top:55px">Get in touch<br>with us!</div>
  <div class="bio" style="left:180px;top:85px;color:#333">Trovanek Lawyers AG<br>Seestrasse 42 – CH-8800 Thalwil<br>+41 44 000 12 34 – contact@trovanek.com<br>Thalwil<br>Horgen<br>Zurich</div>
  <div class="abs" style="left:180px;top:117px;font-size:3.4px;color:#1f6fbf">&#9632; Profile page</div>
</section>

</body>
</html>
```